Web site homepage

I need a new homepage designing for a consumer based IT project

The obvious web sites I like are comparison sites, as they clearly work. See http://www.pricelarder.example/shopping/ca/anti-virus-security-data-protection-c610167/

However this isn’t as clean as it could be as its not their primary revenue stream. However the “results” page for one of the internal pages, should have a theme like this. You will see that by clicking on the product’s image, it takes you straight to the vendor’s check out page – which is exactly the same for the results by on my web site.

Although a completely different market, I like the https://www.quellbrook.example/ web site for its simplicity in selecting your product (pay day loan amount), through to transaction completion. Has a very consumer and friendly feel to it.

I have attached some previous designs which were ok, but not great. I don't want the 4 boxes in the middle anymore but I do like the feel with the top page images

I have also attached a jpeg of the logo I wish to use
Updates

Project Deadline Extended
Reason: A lot of the designs seem to have missed that I DO NOT require the 4 selection boxes as provided in the previous designs I issued as a guide. I am subsequently getting a lot of designs that contain this. I also seem to have a lot of designs which include product images. I DO NOT want these (at this time). The initial purpose of the site is informational. I am extending the deadline so that I can give feedback to each design and for you to provide a response. I will not extend past these extra 5 days. Thanks

Hello designers, Thank you all for the efforts you have gone to, it is appreciated. I have reviewed each an every design giving my honest feedback. If you have not received the feedback, please contact me. I have extended the deadline - and WILL NOT be extending this any further. I will be reviewing each updated design at this time every evening until the contest closes to give you the feedback as quickly as possible. Thanks for your efforts and please contact me to discuss any points. Gareth.

Target Market(s)

Shieldwise Hub will be an affiliate based web site providing a product comparison-based service for the consumer market, specifically for the UK. Target audience is 100% consumer and should be easy, friendly and memorable for the user.

Industry/Entity Type

Loan

Font styles to use
Sans Serif

Colors

Designer to choose colors to be used in the design.

Requirements
Must have
• Much be a bold, friendly and simple layout
Should not have
• corporate feel. must be consumer focused. bold and simple

```html
<!DOCTYPE html>
<html lang="en">
<head>
<meta charset="utf-8">
<title>Shieldwise Hub</title>
<link rel="stylesheet" href="https://fonts.googleapis.com/css2?family=Carlito:wght@400;700&family=Philosopher:wght@400&family=Damion&family=Arimo:wght@400&display=swap">
<style>
:root{
  --ink:#111;
  --navy:#1f4e8c;
  --nav-dark:#2b2b2b;
  --nav-blue:#1d4f8f;
  --orange:#f39a12;
  --rule:#222;
  --footer:#c2c2c2;
  --white:#fff;
}
*{margin:0;padding:0;box-sizing:border-box}
html,body{width:1200px;height:1087px;overflow:hidden;background:var(--white)}
body{position:relative;font-family:"Carlito",Calibri,sans-serif;color:var(--ink)}
.abs{position:absolute}
.topbar{left:0;top:0;width:1200px;height:9px;background:#0c0c0c}
.utility{left:0;top:0}
.utility-links{left:482px;top:11px;font-family:"Arimo",Arial,sans-serif;font-size:12px;color:#fff;word-spacing:1px}
.utility-links span{margin:0 5px}
.buy-now{left:977px;top:6px;width:55px;height:20px;background:var(--orange);color:#fff;font-family:"Arimo",Arial,sans-serif;font-size:9.5px;line-height:20px;text-align:center;border-radius:2px}
.brand{left:172px;top:40px;display:flex;align-items:center;gap:12px}
.brand-mark{width:52px;height:52px;border-radius:50%;background:var(--navy)}
.brand-name{font-size:30px;font-weight:700;color:var(--navy);line-height:1}
.nav{left:0;top:94px}
.nav a{position:absolute;top:0;height:34px;color:#fff;text-decoration:none;font-size:13.5px;line-height:38px;text-align:center;letter-spacing:.2px}
.rule{background:var(--rule);height:2px}
.hero-art{left:160px;top:132px;width:500px;height:328px;background:radial-gradient(circle at 30% 38%,#ffd36b 0,#f7931e 26%,#fff2c4 48%,#fff 72%)}
.hero-photo{left:892px;top:132px;width:130px;height:330px;background:linear-gradient(180deg,#f1dcc5 0,#e8c9a4 30%,#26262b 60%,#111 100%);border-radius:65px 65px 0 0}
.tagline{left:585px;top:200px;width:305px;text-align:center;font-family:"Damion",cursive;font-size:37px;color:var(--navy);z-index:2}
.hero-title{left:580px;top:266px;width:305px;text-align:center;font-family:"Philosopher",sans-serif;font-size:33px;line-height:38px;color:var(--ink);z-index:2}
.intro{left:157px;top:482px;width:495px;font-size:20px;line-height:27px}
.divider-v{width:1px;background:#333}
.promo{left:741px;top:490px;font-size:20px;line-height:27px}
.feature{top:609px;width:170px;text-align:center}
.feature svg{display:block;margin:0 auto}
.feature p{margin-top:18px;font-size:14.5px;line-height:21px;letter-spacing:.2px}
.section-title{font-size:19px;top:785px}
.item-text{width:210px;font-size:12.5px;line-height:21px}
.bullets{left:814px;top:830px;list-style:none;font-size:14.5px}
.bullets li{position:relative;padding-left:17px;margin-bottom:13px;line-height:15px;width:250px}
.bullets li::before{content:"";position:absolute;left:2px;top:6px;width:4px;height:4px;border-radius:50%;background:var(--ink)}
.footer{left:0;top:1032px;width:1200px;height:55px;background:var(--footer);font-family:"Arimo",Arial,sans-serif;font-size:11.5px;color:#222}
.footer-links{position:absolute;left:151px;top:18px}
.footer-links span{margin:0 6px}
.footer-legal{position:absolute;right:138px;top:18px}
</style>
</head>
<body>
<div class="abs topbar"></div>
<svg class="abs utility" width="1200" height="40" aria-hidden="true"><polygon points="424,9 1044,9 1044,33 448,33" fill="#0c0c0c"/></svg>
<div class="abs utility-links">Support<span>|</span>FAQs<span>|</span>Site Map<span>|</span>Help</div>
<div class="abs buy-now">BUY NOW</div>

<div class="abs brand"><div class="brand-mark"></div><div class="brand-name">Shieldwise Hub</div></div>

<svg class="abs nav" width="1200" height="36" aria-hidden="true">
  <polygon points="399,34 414,0 515,0 529,34" fill="var(--nav-blue)"/>
  <polygon points="529,34 545,0 704,0 719,34" fill="var(--nav-dark)"/>
  <polygon points="719,34 735,0 836,0 851,34" fill="var(--nav-dark)"/>
  <polygon points="851,34 867,0 1030,0 1045,34" fill="var(--nav-dark)"/>
</svg>
<nav class="abs nav" style="width:1200px;height:34px">
  <a href="#" style="left:399px;width:130px">VENDORS</a>
  <a href="#" style="left:529px;width:190px">PROTECTION TYPES</a>
  <a href="#" style="left:719px;width:132px">PRODUCTS</a>
  <a href="#" style="left:851px;width:194px">SHIELDWISE HUB</a>
</nav>
<div class="abs rule" style="left:154px;top:127px;width:891px"></div>

<div class="abs hero-art" role="img" aria-label="Illustration of a glowing orange globe beside a laptop showing a striped security shield"></div>
<div class="abs hero-photo" role="img" aria-label="Photo of a smiling advisor in a dark suit holding a notebook"></div>
<div class="abs tagline">Simply Evolution...</div>
<div class="abs hero-title">Keep Your PC Free<br>From Virus</div>
<div class="abs rule" style="left:154px;top:462px;width:891px"></div>

<p class="abs intro">Lorem ipsum dolor sit amet, consectetuer adipiscing elit. Donec quam felis, ultricies nec, pellentesque eu, pretium quis, sem.</p>
<div class="abs divider-v" style="left:659px;top:475px;height:77px;width:2px;background:#222"></div>
<svg class="abs" style="left:676px;top:475px" width="54" height="76" viewBox="0 0 54 76" aria-hidden="true" fill="none" stroke="#111" stroke-width="2.5">
  <path d="M27 3a23 23 0 0 0-14 41c4 4 7 8 8 13h12c1-5 4-9 8-13A23 23 0 0 0 27 3z"/>
  <path d="M20 60h14M21 65h12M23 70h8"/>
</svg>
<p class="abs promo">Is Shieldwise Hub right for you?<br>Find out more</p>
<div class="abs rule" style="left:154px;top:572px;width:891px"></div>

<div class="abs feature" style="left:150px">
  <svg width="60" height="66" viewBox="0 0 60 66" fill="none" stroke="var(--navy)" stroke-width="2.5" aria-hidden="true">
    <rect x="12" y="2" width="7" height="62"/><rect x="38" y="2" width="7" height="62"/>
    <circle cx="15.5" cy="44" r="11" fill="#fff"/><circle cx="41.5" cy="22" r="11" fill="#fff"/>
  </svg>
  <p>CHOOSE HOW MUCH,<br>FOR HOW LONG</p>
</div>
<div class="abs feature" style="left:332px">
  <svg width="70" height="70" viewBox="0 0 70 70" fill="none" stroke="var(--navy)" stroke-width="4" aria-hidden="true">
    <circle cx="35" cy="35" r="32"/><path d="M35 35L18 25M35 35L52 25" stroke-width="3"/>
  </svg>
  <p style="margin-top:14px">APPLY ONLINE<br>ANYTIME 24/7</p>
</div>
<div class="abs feature" style="left:502px">
  <svg width="50" height="66" viewBox="0 0 50 66" aria-hidden="true">
    <rect x="2" y="0" width="46" height="5" fill="var(--navy)"/><rect x="2" y="61" width="46" height="5" fill="var(--navy)"/>
    <path d="M8 5h34L25 33 42 61H8L25 33z" fill="none" stroke="var(--navy)" stroke-width="3"/>
    <path d="M14 58h22L25 42z" fill="var(--navy)"/>
  </svg>
  <p>ONLINE<br>DECISION</p>
</div>
<div class="abs feature" style="left:671px">
  <svg width="70" height="68" viewBox="0 0 70 68" aria-hidden="true" fill="var(--navy)">
    <rect x="0" y="24" width="6" height="18"/><rect x="7" y="20" width="14" height="26"/>
    <polygon points="23,20 63,2 63,62 23,46"/><rect x="64" y="0" width="5" height="64"/>
    <rect x="11" y="48" width="11" height="18"/>
  </svg>
  <p>SEE THE FULL<br>COST UPFRONT</p>
</div>
<div class="abs feature" style="left:856px;width:180px">
  <svg width="68" height="68" viewBox="0 0 68 68" aria-hidden="true">
    <rect x="2" y="7" width="64" height="59" fill="none" stroke="var(--navy)" stroke-width="3"/>
    <rect x="2" y="18" width="64" height="3" fill="var(--navy)"/>
    <rect x="14" y="1" width="5" height="12" fill="var(--navy)"/><rect x="49" y="1" width="5" height="12" fill="var(--navy)"/>
    <text x="34" y="58" text-anchor="middle" font-family="Carlito,sans-serif" font-size="32" fill="var(--navy)">10</text>
  </svg>
  <p>ONLY PAY INTEREST FOR<br>THE DAYS YOU BORROW</p>
</div>
<div class="abs rule" style="left:154px;top:766px;width:891px"></div>

<h2 class="abs section-title" style="left:155px;font-weight:400">Phasellus viverra nulla ut metus</h2>
<svg class="abs" style="left:151px;top:836px" width="66" height="66" viewBox="0 0 66 66" aria-hidden="true">
  <circle cx="28" cy="28" r="24" fill="none" stroke="#111" stroke-width="5"/><path d="M45 45l17 17" stroke="#111" stroke-width="7" stroke-linecap="round"/>
</svg>
<p class="abs item-text" style="left:229px;top:833px">In enim justo, rhoncus ut, imperdiet a, venenatis vitae, justo. Nullam dictum felis eu pede mollis pretium.</p>
<svg class="abs" style="left:463px;top:832px" width="62" height="70" viewBox="0 0 62 70" aria-hidden="true">
  <rect x="8" y="4" width="46" height="62" fill="#111" transform="rotate(5 31 35)"/>
  <rect x="5" y="2" width="46" height="62" fill="#111"/>
  <g stroke="#fff" stroke-width="1.5"><path d="M11 12h34M11 19h34M11 26h34M11 33h34M11 40h34M11 47h34M11 54h34"/></g>
</svg>
<p class="abs item-text" style="left:552px;top:830px">In enim justo, rhoncus ut, imperdiet a, venenatis vitae, justo. Nullam dictum felis eu pede mollis pretium.</p>
<svg class="abs" style="left:151px;top:935px" width="52" height="70" viewBox="0 0 52 70" aria-hidden="true">
  <path d="M12 30V18a14 14 0 0 1 28 0v12" fill="none" stroke="#111" stroke-width="6"/>
  <rect x="2" y="30" width="48" height="39" rx="3" fill="#111"/>
  <circle cx="26" cy="47" r="4" fill="#fff"/><rect x="24.5" y="47" width="3" height="9" fill="#fff"/>
</svg>
<p class="abs item-text" style="left:229px;top:948px">In enim justo, rhoncus ut, imperdiet a, venenatis vitae, justo. Nullam dictum felis eu pede mollis pretium.</p>
<svg class="abs" style="left:457px;top:925px" width="80" height="72" viewBox="0 0 80 72" aria-hidden="true">
  <path d="M40 5L76 67H4z" fill="none" stroke="#111" stroke-width="6" stroke-linejoin="round"/>
  <rect x="36" y="24" width="8" height="25" rx="2" fill="#111"/><circle cx="40" cy="57" r="5" fill="#111"/>
</svg>
<p class="abs item-text" style="left:552px;top:938px">In enim justo, rhoncus ut, imperdiet a, venenatis vitae, justo. Nullam dictum felis eu pede mollis pretium.</p>

<div class="abs divider-v" style="left:779px;top:831px;height:182px"></div>
<h2 class="abs section-title" style="left:814px;font-weight:400">Maecenas nec odio et</h2>
<ul class="abs bullets">
  <li>Integer tincidunt.</li>
  <li style="margin-top:20px">Cras dapibus.</li>
  <li style="margin-top:20px">Vivamus elementum semper nisi.</li>
  <li style="margin-top:20px">Aenean vulputate eleifend tellus.</li>
  <li style="margin-top:20px">Aenean leo ligula, porttitor eu, consequat vitae, eleifend ac, enim.</li>
</ul>

<footer class="abs footer">
  <div class="footer-links">Help<span>|</span>Privacy Policy<span>|</span>Terms &amp; Conditions</div>
  <div class="footer-legal">shieldwisehub.example, Larkfield Court, Venenatis, CH9 4QX. © shieldwisehub.example 2015</div>
</footer>
</body>
</html>
```